Business Card design for Founder and CEO of new shoe company

I am looking for a business card design for my new shoe company called Strapwell.

I am launching the company this April. Strapwell shoes offers slip-on athletic and casual style shoes for men and women. The unique selling point of the brand is that all of our shoe exist without shoelaces. I have included a link to the website to offer additional information about the company, see product images, and gain inspiration for the design. You can use the store owner password "Strapwell" to access the website.

www.Strapwell.example

Thanks,
Dan Hollis

Target Market(s)

Active Men and Women ages 16-45

Industry/Entity Type

Business

Contact Information for Business Card

Dan Hollis
Founder and CEO
www.Strapwell.example
danhollis@Strapwell.example
888-555-0187 / 888-5STRAPW
Strapwell, LLC
2284 N Tamsin Ave
Chicago, IL 60699

Requirements
Must have
• Be able to quickly and easily tell that Strapwell is a shoe company from the business card

```html
<!DOCTYPE html>
<html lang="en">
<head>
<meta charset="utf-8">
<title>Strapwell Business Card</title>
<link rel="stylesheet" href="https://fonts.googleapis.com/css2?family=Roboto:wght@300;400;500;700&family=Roboto+Slab:wght@700&display=swap">
<style>
  :root {
    --page-bg: #ece8e1;
    --card-blue-light: #3a8fd6;
    --card-blue-dark: #1f68b4;
    --title-blue: #a9d2f5;
    --white: #ffffff;
    --ink: #111111;
    --muted-grey: #6f6f6f;
    --photo-dark: #3b2a28;
    --photo-mid: #5b3a34;
    --photo-blue: #2d7fd0;
    --shoe-grey: #b9bcc0;
    --shoe-blue: #2f96dd;
    --floor-dark: #2a2a2c;
  }
  html, body {
    margin: 0;
    padding: 0;
    width: 1200px;
    height: 375px;
    overflow: hidden;
    background: var(--page-bg);
  }
  .canvas {
    position: relative;
    width: 1200px;
    height: 375px;
    font-family: "Roboto", Arial, sans-serif;
  }
  .card {
    position: absolute;
    top: 37px;
    width: 525px;
    height: 300px;
    overflow: hidden;
    box-shadow: 0 2px 6px rgba(0,0,0,0.18);
  }
  /* Front */
  .card-front { left: 47px; background: linear-gradient(160deg, var(--card-blue-light), var(--card-blue-dark)); }
  .contact { position: absolute; left: 81px; top: 40px; color: var(--white); }
  .contact-name {
    font-family: "Roboto Slab", Georgia, serif;
    font-weight: 700; font-size: 19px; letter-spacing: 0.5px; margin: 0;
  }
  .contact-title { margin: 6px 0 0; font-size: 14px; font-weight: 700; color: var(--title-blue); }
  .contact-lines { margin: 24px 0 0; font-size: 14px; line-height: 20.5px; font-weight: 400; }
  .contact-company { margin: 22px 0 0; font-size: 14px; line-height: 20px; }
  .contact-company strong { font-weight: 700; }
  .front-photo {
    position: absolute; left: 380px; top: 0; width: 145px; height: 300px;
    background: linear-gradient(180deg, var(--photo-dark) 0%, var(--photo-mid) 35%, var(--photo-blue) 55%, var(--photo-dark) 100%);
  }
  .front-wordmark {
    position: absolute; left: 486px; top: 282px;
    transform: rotate(-90deg); transform-origin: left top;
    color: var(--white); font-size: 30px; font-weight: 300; letter-spacing: 1px;
    white-space: nowrap;
  }
  /* Back */
  .card-back { left: 620px; background: var(--white); }
  .back-wordmark {
    position: absolute; left: 30px; top: 30px;
    display: flex; align-items: center; gap: 16px;
    font-size: 50px; font-weight: 300; color: var(--ink); letter-spacing: 2px;
  }
  .back-wordmark .mark { width: 34px; height: 34px; background: var(--ink); }
  .back-photo {
    position: absolute; left: 0; top: 100px; width: 525px; height: 200px;
    background:
      radial-gradient(ellipse 40% 55% at 72% 45%, var(--shoe-blue) 0%, rgba(47,150,221,0) 100%),
      radial-gradient(ellipse 35% 45% at 35% 40%, var(--shoe-grey) 0%, rgba(185,188,192,0) 100%),
      linear-gradient(180deg, #f4f4f4 0%, #e2e2e2 45%, var(--floor-dark) 62%, var(--floor-dark) 100%);
  }
  .back-url {
    position: absolute; left: 44px; top: 268px;
    color: var(--white); font-size: 14px; font-weight: 400;
  }
</style>
</head>
<body>
<div class="canvas">
  <section class="card card-front">
    <div class="contact">
      <h1 class="contact-name">Dan Hollis</h1>
      <p class="contact-title">Founder and CEO</p>
      <p class="contact-lines">
        www.Strapwell.example<br>
        danhollis@Strapwell.example<br>
        <svg width="11" height="11" viewBox="0 0 24 24" aria-hidden="true" style="vertical-align:-1px"><path fill="none" stroke="#fff" stroke-width="2.4" d="M6 2l4 5-2 3c1 3 3 5 6 6l3-2 5 4-2 4C11 21 3 13 3 5z"/></svg>
        888-555-0187 / 888-5STRAPW
      </p>
      <p class="contact-company">
        <strong>Strapwell, LLC</strong><br>
        2284 N Tamsin Ave<br>
        Chicago, IL 60699
      </p>
    </div>
    <div class="front-photo" role="img" aria-label="Photo of feet wearing blue slip-on athletic shoes"></div>
    <div class="front-wordmark">Strapwell</div>
  </section>

  <section class="card card-back">
    <div class="back-photo" role="img" aria-label="Photo of a grey and a blue slip-on running shoe side by side"></div>
    <div class="back-wordmark"><span class="mark"></span>Strapwell</div>
    <div class="back-url">www.Strapwell.example</div>
  </section>
</div>
</body>
</html>
```